Kestrel Softball Tournaments Website Design

Our client would like us to design a website. The company is similar to Brightfield Sports USA (https://brightfieldsportsusa.example).

We prefer Adobe Fonts in the design. Lorem ipsum is fine to use for content, except for headers. Please keep track of any images used in your design. We plan on purchasing the images used.

Number of Pages Required

1 page

Font styles to use
Sans Serif

Colors
0054AA
0677BA
7BADD7
CADEEF
E8F1F8

```html
<!DOCTYPE html>
<html lang="en">
<head>
<meta charset="utf-8">
<title>Kestrel Softball Tournaments — Website Design</title>
<link rel="stylesheet" href="https://fonts.googleapis.com/css2?family=Roboto+Condensed:wght@400;500;700&family=Roboto:wght@400;500&display=swap">
<style>
  :root {
    --blue-deep: #0054AA;
    --blue: #0677BA;
    --blue-mid: #7BADD7;
    --blue-light: #CADEEF;
    --blue-pale: #E8F1F8;
    --stage: #B9CFE2;
    --white: #ffffff;
    --ink: #222831;
    --ink-soft: #5b6470;
    --line: #d6dde4;
  }
  * { box-sizing: border-box; margin: 0; padding: 0; }
  html, body { width: 1200px; height: 568px; overflow: hidden; }
  body {
    background: var(--stage);
    font-family: "Roboto", Arial, sans-serif;
    color: var(--ink);
    position: relative;
  }
  .page {
    position: absolute;
    background: var(--white);
    width: 366px;
    overflow: hidden;
    box-shadow: 0 0 6px rgba(40, 70, 110, .25);
  }
  .page--home { left: 28px; top: 108px; height: 460px; }
  .page--events { left: 423px; top: 0; height: 568px; }
  .page--footer { left: 815px; top: 0; height: 442px; }
  .abs { position: absolute; }

  .heading {
    font-family: "Roboto Condensed", Arial, sans-serif;
    color: var(--blue);
    font-weight: 400;
    text-transform: uppercase;
    letter-spacing: .2px;
  }
  .body-text { font-size: 4.4px; line-height: 5.6px; color: var(--ink-soft); }
  .btn-outline {
    position: absolute; border: .6px solid var(--blue); color: var(--blue);
    font-size: 3.4px; text-transform: uppercase; display: flex; align-items: center; justify-content: center;
    background: var(--white);
  }
  .btn-solid {
    position: absolute; background: var(--blue); color: var(--white);
    font-size: 3.6px; text-transform: uppercase; display: flex; align-items: center; justify-content: center;
  }
  .photo { position: absolute; }

  /* header */
  .site-header { position: absolute; left: 0; top: 0; width: 366px; height: 26px; }
  .brand { position: absolute; left: 24px; top: 7px; display: flex; align-items: center; gap: 3px; }
  .brand-mark { width: 9px; height: 9px; border-radius: 50%; background: var(--blue-deep); }
  .brand-name { font-family: "Roboto Condensed", Arial, sans-serif; font-weight: 700; font-size: 8px; color: var(--blue-deep); }
  .nav { position: absolute; left: 103px; top: 8px; display: flex; gap: 4px; }
  .nav a { font-size: 3.8px; color: var(--ink); text-decoration: none; height: 9px; padding: 0 3px; display: flex; align-items: center; }
  .nav a.is-active { background: var(--blue); color: var(--white); }
  .social { position: absolute; display: flex; gap: 4px; }
  .social span { width: 11px; height: 11px; border-radius: 50%; border: .6px solid var(--blue-deep); display: flex; align-items: center; justify-content: center; }

  .search { position: absolute; left: 91px; top: 237px; width: 194px; height: 16px; display: flex; }
  .search-field { flex: 1; border: .6px solid var(--blue-mid); display: flex; align-items: center; gap: 4px; padding-left: 5px; font-size: 4px; color: var(--blue-mid); }
  .search-btn { width: 36px; background: var(--blue); color: var(--white); font-size: 3.8px; display: flex; align-items: center; justify-content: center; }

  .band { position: absolute; left: 0; width: 366px; background: var(--blue-pale); }

  /* events */
  .event-date { position: absolute; background: var(--blue-deep); color: var(--white); font-size: 3.4px; width: 57px; height: 9px; display: flex; align-items: center; justify-content: center; }
  .event-title { position: absolute; font-size: 7px; color: var(--ink); }
  .event-venue { position: absolute; font-size: 3.8px; color: var(--ink-soft); display: flex; align-items: center; gap: 3px; }

  /* sponsors */
  .sponsor { position: absolute; width: 72px; text-align: center; }
  .sponsor-badge { width: 48px; height: 48px; border-radius: 50%; background: var(--white); margin: 0 auto 4px; display: flex; align-items: center; justify-content: center; }
  .sponsor-badge span { width: 18px; height: 18px; border-radius: 3px; background: #d3322e; }
  .sponsor-label { font-size: 5px; line-height: 6.4px; color: var(--ink); }

  .footer-links { position: absolute; list-style: none; font-size: 3.4px; line-height: 7.8px; color: var(--ink); text-transform: uppercase; }
  .footer-note { position: absolute; left: 0; width: 365px; text-align: center; font-size: 3.2px; line-height: 4.6px; color: var(--ink-soft); }
</style>
</head>
<body>

<!-- Home page: header, hero, search, about -->
<section class="page page--home">
  <header class="site-header">
    <div class="brand"><span class="brand-mark"></span><span class="brand-name">KESTREL</span></div>
    <nav class="nav">
      <a class="is-active">HOME</a><a>ABOUT US</a><a>UPCOMING</a><a>HOTELS</a><a>CONTACT</a>
    </nav>
    <div class="btn-solid" style="left:231px;top:8px;width:33px;height:10px;">Register Now</div>
    <div class="social" style="left:294px;top:7px;">
      <span><svg width="6" height="5" viewBox="0 0 6 5"><rect x=".3" y=".3" width="5.4" height="4.4" fill="none" stroke="#0054AA" stroke-width=".6"/><path d="M.3 .3 3 2.8 5.7 .3" fill="none" stroke="#0054AA" stroke-width=".6"/></svg></span>
      <span></span><span></span>
    </div>
  </header>

  <div class="photo" role="img" aria-label="Softball team holding bats in a locker room" style="left:0;top:26px;width:366px;height:194px;background:linear-gradient(135deg,#3a2c22 0%,#6b5746 45%,#4a3a2e 70%,#2a201a 100%);"></div>

  <div class="search">
    <div class="search-field">
      <svg width="7" height="7" viewBox="0 0 7 7"><circle cx="3" cy="3" r="2.3" fill="none" stroke="#7BADD7" stroke-width=".7"/><path d="M4.7 4.7 6.6 6.6" stroke="#7BADD7" stroke-width=".7"/></svg>
      Search an event
    </div>
    <div class="search-btn">SEARCH</div>
  </div>

  <div class="band" style="top:269px;height:140px;"></div>
  <h2 class="heading abs" style="left:34px;top:304px;font-size:11px;color:var(--blue-deep);">About Us</h2>
  <p class="body-text abs" style="left:34px;top:321px;width:112px;">Lorem ipsum dolor sit amet, consectetur adipiscing elit, sed do eiusmod tempor incididunt ut labore et dolore magna aliqua. Ut enim ad minim veniam, quis nostrud exercitation ullamco laboris nisi ut aliquip ex ea commodo consequat.</p>
  <div class="btn-outline" style="left:34px;top:363px;width:39px;height:9px;">Read More</div>
  <div class="photo" role="img" aria-label="Softball player resting a bat on his shoulders" style="left:152px;top:283px;width:181px;height:137px;background:linear-gradient(180deg,#9cc3e6 0%,#c7dcee 40%,#6f7f8c 70%,#3d4650 100%);"></div>
</section>

<!-- Events page: upcoming list, how it works, join -->
<section class="page page--events">
  <h2 class="heading abs" style="left:0;width:365px;text-align:center;top:16px;font-size:11px;">Upcoming Tournements</h2>

  <div class="photo" role="img" aria-label="Softball team in a locker room" style="left:53px;top:43px;width:52px;height:52px;background:linear-gradient(135deg,#5a4838,#8d7865,#3d3028);"></div>
  <div class="event-date" style="left:118px;top:43px;">3:00 PM, 21st March 2023</div>
  <div class="event-title" style="left:118px;top:59px;">Event name comes here</div>
  <p class="body-text abs" style="left:118px;top:68px;width:210px;">Lorem ipsum dolor sit amet, consectetur adipiscing elit, sed do eiusmod tempor incididunt ut labore et dolore magna aliqua.</p>
  <div class="btn-outline" style="left:118px;top:86px;width:38px;height:9px;">Read More</div>
  <div class="event-venue" style="left:165px;top:87px;"><svg width="5" height="6" viewBox="0 0 5 6"><path d="M2.5 5.8C1 4 .4 3 .4 2.1a2.1 2.1 0 0 1 4.2 0c0 .9-.6 1.9-2.1 3.7z" fill="none" stroke="#5b6470" stroke-width=".5"/><circle cx="2.5" cy="2.1" r=".7" fill="#5b6470"/></svg>Lorem ipsum dolor sit amet</div>

  <div class="photo" role="img" aria-label="Softball team in a locker room" style="left:53px;top:116px;width:52px;height:52px;background:linear-gradient(135deg,#5a4838,#8d7865,#3d3028);"></div>
  <div class="event-date" style="left:118px;top:116px;">3:00 PM, 21st March 2023</div>
  <div class="event-title" style="left:118px;top:132px;">Event name comes here</div>
  <p class="body-text abs" style="left:118px;top:141px;width:210px;">Lorem ipsum dolor sit amet, consectetur adipiscing elit, sed do eiusmod tempor incididunt ut labore et dolore magna aliqua.</p>
  <div class="btn-outline" style="left:118px;top:159px;width:38px;height:9px;">Read More</div>
  <div class="event-venue" style="left:165px;top:160px;"><svg width="5" height="6" viewBox="0 0 5 6"><path d="M2.5 5.8C1 4 .4 3 .4 2.1a2.1 2.1 0 0 1 4.2 0c0 .9-.6 1.9-2.1 3.7z" fill="none" stroke="#5b6470" stroke-width=".5"/><circle cx="2.5" cy="2.1" r=".7" fill="#5b6470"/></svg>Lorem ipsum dolor sit amet</div>

  <div class="photo" role="img" aria-label="Softball team in a locker room" style="left:53px;top:188px;width:52px;height:52px;background:linear-gradient(135deg,#5a4838,#8d7865,#3d3028);"></div>
  <div class="event-date" style="left:118px;top:188px;">3:00 PM, 21st March 2023</div>
  <div class="event-title" style="left:118px;top:204px;">Event name comes here</div>
  <p class="body-text abs" style="left:118px;top:213px;width:210px;">Lorem ipsum dolor sit amet, consectetur adipiscing elit, sed do eiusmod tempor incididunt ut labore et dolore magna aliqua.</p>
  <div class="btn-outline" style="left:118px;top:231px;width:38px;height:9px;">Read More</div>
  <div class="event-venue" style="left:165px;top:232px;"><svg width="5" height="6" viewBox="0 0 5 6"><path d="M2.5 5.8C1 4 .4 3 .4 2.1a2.1 2.1 0 0 1 4.2 0c0 .9-.6 1.9-2.1 3.7z" fill="none" stroke="#5b6470" stroke-width=".5"/><circle cx="2.5" cy="2.1" r=".7" fill="#5b6470"/></svg>Lorem ipsum dolor sit amet</div>

  <div class="btn-solid" style="left:163px;top:258px;width:38px;height:12px;">View All Events</div>

  <div class="band" style="top:310px;height:139px;"></div>
  <div class="photo" role="img" aria-label="Team hands stacked together under a blue sky" style="left:41px;top:324px;width:164px;height:137px;background:linear-gradient(160deg,#c94a4a 0%,#b9d3ec 35%,#e7eef6 60%,#c75050 100%);"></div>
  <h2 class="heading abs" style="left:222px;top:346px;font-size:11px;">How It Works</h2>
  <p class="body-text abs" style="left:222px;top:362px;width:106px;">Lorem ipsum dolor sit amet, consectetur adipiscing elit, sed do eiusmod tempor incididunt ut labore et dolore magna aliqua. Ut enim ad minim veniam, quis nostrud exercitation ullamco laboris nisi ut aliquip ex ea commodo consequat.</p>
  <div class="btn-outline" style="left:222px;top:404px;width:38px;height:9px;">Read More</div>

  <h2 class="heading abs" style="left:0;width:365px;text-align:center;top:500px;font-size:11px;">Join and Enjoy With Us</h2>
  <div class="photo" role="img" aria-label="Pitcher holding a softball on the field, video preview" style="left:53px;top:521px;width:257px;height:60px;background:linear-gradient(180deg,#c8c4bc 0%,#a99c88 60%,#8c7e6a 100%);"></div>
</section>

<!-- Lower page: video, sponsors, footer -->
<section class="page page--footer">
  <div class="photo" role="img" aria-label="Pitcher holding a softball on the field, video preview" style="left:55px;top:7px;width:257px;height:125px;background:linear-gradient(180deg,#d2cfc9 0%,#b2a792 55%,#8a7b66 100%);"></div>
  <svg class="abs" style="left:172px;top:59px;" width="22" height="22" viewBox="0 0 22 22"><circle cx="11" cy="11" r="10" fill="rgba(255,255,255,.25)" stroke="#fff" stroke-width="1"/><path d="M9 7v8l6-4z" fill="#fff"/></svg>

  <div class="band" style="top:172px;height:135px;background:var(--blue-light);"></div>
  <h2 class="heading abs" style="left:0;width:365px;text-align:center;top:195px;font-size:11px;color:var(--blue-deep);">Our Sponsors</h2>
  <div class="sponsor" style="left:43px;top:217px;"><div class="sponsor-badge"><span></span></div><div class="sponsor-label">Official Uniform<br>Partner</div></div>
  <div class="sponsor" style="left:110px;top:217px;"><div class="sponsor-badge"><span></span></div><div class="sponsor-label">Official Transport<br>Partner</div></div>
  <div class="sponsor" style="left:178px;top:217px;"><div class="sponsor-badge"><span></span></div><div class="sponsor-label">Official Accomodation<br>Partner</div></div>
  <div class="sponsor" style="left:250px;top:217px;"><div class="sponsor-badge"><span></span></div><div class="sponsor-label">Official Broadcasting<br>Partner</div></div>

  <div class="abs" style="left:0;top:341px;width:365px;height:.6px;background:var(--line);"></div>
  <div class="brand" style="left:58px;top:366px;"><span class="brand-mark" style="width:7px;height:7px;"></span><span class="brand-name" style="font-size:6px;">KESTREL</span></div>
  <ul class="footer-links" style="left:139px;top:356px;"><li>Home</li><li>About Us</li><li>Upcoming</li><li>Hotels</li><li>Contact</li></ul>
  <ul class="footer-links" style="left:166px;top:356px;"><li>How It Works</li><li>Terms and Conditions</li><li>FAQ</li></ul>
  <div class="abs" style="left:253px;top:358px;font-size:3.8px;text-transform:uppercase;color:var(--ink);">Subscribe our newsletter</div>
  <div class="abs" style="left:253px;top:368px;width:61px;height:8px;border:.6px solid var(--ink-soft);font-size:3px;color:var(--ink-soft);padding-left:2px;line-height:7px;">E-Mail</div>
  <div class="btn-solid" style="left:253px;top:380px;width:34px;height:11px;">Subscribe</div>

  <div class="social" style="left:162px;top:410px;">
    <span><svg width="6" height="5" viewBox="0 0 6 5"><rect x=".3" y=".3" width="5.4" height="4.4" fill="none" stroke="#0054AA" stroke-width=".6"/><path d="M.3 .3 3 2.8 5.7 .3" fill="none" stroke="#0054AA" stroke-width=".6"/></svg></span>
    <span></span><span></span>
  </div>
  <p class="footer-note" style="top:430px;">Lorem ipsum dolor sit amet, consectetur adipiscing elit, sed do eiusmod tempor incididunt ut labore et dolore magna aliqua. Ut enim ad minim veniam,<br>quis nostrud exercitation ullamco laboris nisi ut aliquip ex ea commodo consequat.</p>
</section>

</body>
</html>
```